1 Landingpage plus 2 passende Newsletter-Templates (Responsive)
Zielgruppe
Wir sind ein deutscher E-Mail- und Clouddienstleister, unsere Zielgruppe sind in erster Linie Privatkunden.
Aufgabenstellung
Für eine noch zu startende, erfolgreiche Marketingkampagne, benötigen wir für eines unserer Produkte insgesamt zwei unterschiedliche Newsletter-Templates (A/B-Test) und eine optisch dazu passende Landingpage inkl. Registrierungsformular. Die Anbindung an unser System übernehmen wir selbst.
Newslettertemplates sowie Landingpage sollen so einfach wie möglich, dennoch werbewirksam und nach heutigen Kriterien und Maßstäben entworfen und hergestellt werden (Responsive, Beachtung gängiger E-Mailstandards und -clients).
Die Ausgestaltung von Text und Grafik sollte von jemandem durchgeführt werden, der ggfls. bereits Erfahrung im E-Mailmarketing hat.
Unser eigenes CD/CI muss eingearbeitet bzw. berücksichtigt werden, darf aber "aufgehübscht" und moderner interpretiert werden.
Zu einem späteren Zeitplunkt planen wir den Relaunch unseres Portals, ggfls. ergeben sich weitere Möglichkeiten der Zusammenarbeit.
Unser Logo kann im .SVG-Format bereit gestellt werden.

```html
<!DOCTYPE html>
<html lang="de">
<head>
<meta charset="utf-8">
<title>Nubora Connect – Jetzt anmelden</title>
<link rel="stylesheet" href="https://fonts.googleapis.com/css2?family=Montserrat:wght@400;500;600;700&family=Exo+2:wght@700;800&display=swap">
<style>
:root{
  --orange:#ea5f04;
  --orange-deep:#e03b08;
  --tan:#d9a877;
  --peach:#fdd7a9;
  --field:#f1f1f1;
  --ink:#1c1c1c;
  --muted:#8a8a8a;
  --footer:#4a4a4a;
  --white:#ffffff;
}
*{box-sizing:border-box;margin:0;padding:0}
html,body{width:1200px;height:2250px;overflow:hidden;background:var(--white);font-family:"Montserrat",Arial,sans-serif;color:var(--ink)}
.page{position:relative;width:1200px;height:2250px}
.abs{position:absolute}

/* header */
.site-header{left:0;top:0;width:1200px;height:103px;background:var(--white);border-bottom:1px solid #cdb79c}
.brand{left:112px;top:21px;width:415px;height:65px;background:var(--orange);border-radius:4px;display:flex;align-items:center;gap:18px;padding-left:28px}
.brand-mark{width:26px;height:26px;background:var(--white);border-radius:50%}
.brand-name{font-family:"Montserrat",Arial,sans-serif;font-weight:600;font-size:38px;color:var(--white);letter-spacing:.5px}
.hotline-icon{left:655px;top:18px}
.hotline-number{left:738px;top:6px;font-family:"Exo 2",Arial,sans-serif;font-weight:800;font-size:54px;color:var(--orange);letter-spacing:1px;line-height:1}
.hotline-hours{left:777px;top:67px;font-weight:700;font-size:19px;color:var(--ink)}

/* hero */
.hero{left:0;top:103px;width:1200px;height:711px;background:var(--tan)}
.hero-photo{left:93px;top:103px;width:639px;height:711px;background:linear-gradient(135deg,#e9d2a6 0%,#cfb996 40%,#8f8a7f 70%,#7a5a45 100%)}
.signup{left:732px;top:103px;width:374px;height:711px;background:var(--orange)}
.signup-title{left:732px;top:120px;width:374px;text-align:center;font-weight:700;font-size:56px;line-height:66px;color:var(--white);letter-spacing:1px}
.field{height:51px;background:var(--field);border-radius:3px;color:var(--muted);font-size:20px;padding-left:14px;display:flex;align-items:center}
.submit{left:821px;top:710px;width:194px;height:54px;background:var(--white);border-radius:4px;display:flex;align-items:center;justify-content:center;font-family:"Exo 2",Arial,sans-serif;font-weight:800;font-size:30px;color:var(--orange)}

/* features */
.feature{width:300px;text-align:center}
.feature-icon{width:112px;height:112px;border-radius:50%;background:var(--orange);margin:0 auto;display:flex;align-items:center;justify-content:center}
.feature-title{margin-top:20px;font-weight:700;font-size:37px;line-height:44px}
.feature-text{margin-top:8px;font-size:17.5px;line-height:22px}

/* offer */
.offer{left:0;top:1270px;width:1200px;height:467px;background:var(--peach)}
.offer-title{left:672px;top:1334px;font-weight:700;font-size:49px;color:var(--orange);letter-spacing:1px}
.offer-text{left:672px;width:430px;font-weight:500;font-size:20px;line-height:25.5px;text-align:justify;text-align-last:left;letter-spacing:-.2px}
.offer-visual{left:88px;top:1406px;width:530px;height:215px;border-radius:6px;background:linear-gradient(90deg,#f39a4c 0%,#ea6a12 60%,#e04a0a 100%)}

/* testimonials */
.portrait{width:130px;height:114px;border:5px solid var(--peach);background:linear-gradient(180deg,#e8e4df,#c9bfb4)}
.quote{width:420px;text-align:center;font-size:18.5px;line-height:22px}
.quote-name{width:420px;text-align:center;font-weight:700;font-size:16.5px;color:var(--orange);letter-spacing:.5px}

/* footer */
.site-footer{left:0;top:2196px;width:1200px;height:54px;background:var(--footer);color:var(--white);font-size:17.5px;display:flex;align-items:center;justify-content:center}
</style>
</head>
<body>
<div class="page">

  <header class="site-header abs"></header>
  <div class="brand abs"><span class="brand-mark"></span><span class="brand-name">Nubora Connect</span></div>
  <svg class="hotline-icon abs" width="66" height="66" viewBox="0 0 24 24" aria-hidden="true">
    <path fill="#111" d="M6.6 10.8a15.2 15.2 0 0 0 6.6 6.6l2.2-2.2a1 1 0 0 1 1-.25 11.4 11.4 0 0 0 3.6.6 1 1 0 0 1 1 1V20a1 1 0 0 1-1 1A17 17 0 0 1 3 4a1 1 0 0 1 1-1h3.5a1 1 0 0 1 1 1c0 1.25.2 2.45.6 3.6a1 1 0 0 1-.25 1z"/>
    <path fill="none" stroke="#111" stroke-width="1.6" d="M14 6.5a4 4 0 0 1 3.5 3.5M14 3a7.5 7.5 0 0 1 7 7"/>
  </svg>
  <div class="hotline-number abs">0800 274 6612</div>
  <div class="hotline-hours abs">7 Tage die Woche; 8 - 18 Uhr</div>

  <section class="hero abs"></section>
  <div class="hero-photo abs" role="img" aria-label="Foto: Hand tippt auf einem Laptop mit geöffneter Suchseite auf einem Holztisch"></div>
  <div class="signup abs"></div>
  <h1 class="signup-title abs">JETZT<br>ANMELDEN</h1>
  <div class="field abs" style="left:766px;top:294px;width:145px">Vorname</div>
  <div class="field abs" style="left:925px;top:294px;width:141px">Nachname</div>
  <div class="field abs" style="left:766px;top:359px;width:300px">Adresse</div>
  <div class="field abs" style="left:766px;top:424px;width:300px">Stadt</div>
  <div class="field abs" style="left:766px;top:490px;width:300px">Postleitzahl</div>
  <div class="field abs" style="left:766px;top:558px;width:301px">E-Mail</div>
  <div class="field abs" style="left:766px;top:624px;width:301px">Telefon</div>
  <div class="submit abs">Bestätigen</div>

  <div class="feature abs" style="left:110px;top:900px">
    <div class="feature-icon"><svg width="58" height="40" viewBox="0 0 58 40"><rect x="2" y="2" width="54" height="36" fill="none" stroke="#fff" stroke-width="4"/><path d="M2 2l27 22L56 2M2 38l20-18M56 38L36 20" fill="none" stroke="#fff" stroke-width="4"/></svg></div>
    <h2 class="feature-title">Lorem Ipsum</h2>
    <p class="feature-text">Lorem ipsum dolor sit amet,<br>consetetur sadipscing elitr,<br>sed diam nonumy eirmod<br>tempor invidunt ut labore et</p>
  </div>
  <div class="feature abs" style="left:450px;top:900px">
    <div class="feature-icon"><svg width="72" height="50" viewBox="0 0 72 50"><path fill="#fff" d="M18 48a16 16 0 0 1-2-32 20 20 0 0 1 38 4 14 14 0 0 1 0 28z"/><path fill="var(--orange)" d="M31 18h10v12h8L36 43 23 30h8z"/></svg></div>
    <h2 class="feature-title">Lorem Ipsum</h2>
    <p class="feature-text">Lorem ipsum dolor sit amet,<br>consetetur sadipscing elitr,<br>sed diam nonumy eirmod<br>tempor invidunt ut labore et</p>
  </div>
  <div class="feature abs" style="left:788px;top:900px">
    <div class="feature-icon"><svg width="56" height="56" viewBox="0 0 56 56"><rect x="4" y="18" width="48" height="12" fill="#fff"/><rect x="8" y="32" width="40" height="20" fill="#fff"/><rect x="24" y="18" width="8" height="34" fill="var(--orange)"/><path d="M28 17c-4-10-16-12-16-4s12 4 16 4c4 0 16 4 16-4s-12-6-16 4z" fill="none" stroke="#fff" stroke-width="4"/></svg></div>
    <h2 class="feature-title">Lorem Ipsum</h2>
    <p class="feature-text">Lorem ipsum dolor sit amet,<br>consetetur sadipscing elitr,<br>sed diam nonumy eirmod<br>tempor invidunt ut labore et</p>
  </div>

  <section class="offer abs"></section>
  <div class="offer-visual abs" role="img" aria-label="Produktgrafik: verbundene Kreise mit 20 GB Speicher, 50 Free-SMS, IMAP und WebDav sowie Preisbadge nur 1 € monatlich"></div>
  <h2 class="offer-title abs">LOREM IPSUM</h2>
  <p class="offer-text abs" style="top:1406px">Lorem ipsum dolor sit amet, consetetur sadipscing elitr, sed diam nonumy eirmod tempor invidunt ut labore et</p>
  <p class="offer-text abs" style="top:1506px">Lorem ipsum dolor sit amet, consetetur sadipscing elitr, sed diam nonumy eirmod tempor invidunt ut labore et dolore magna aliquyam erat, sed d gubergren, no sea takimata sanctus est Lorem</p>

  <div class="portrait abs" style="left:274px;top:1836px" role="img" aria-label="Porträtfoto einer Kundin mit Brille"></div>
  <p class="quote abs" style="left:128px;top:1967px">„Lorem ipsum dolor sit amet, consetetur sa-<br>dipscing elitr, sed diam nonumy eirmod<br>tempor invidunt ut labore et“</p>
  <p class="quote-name abs" style="left:128px;top:2045px">LENA HARTWIG</p>

  <div class="portrait abs" style="left:802px;top:1836px" role="img" aria-label="Porträtfoto eines lächelnden Kunden"></div>
  <p class="quote abs" style="left:656px;top:1967px">„Lorem ipsum dolor sit amet, consetetur sa-<br>dipscing elitr, sed diam nonumy eirmod<br>tempor invidunt ut labore et“</p>
  <p class="quote-name abs" style="left:656px;top:2045px">JONAS BREUER</p>

  <footer class="site-footer abs">© Copyright 2017 Lorem ipsum dolor sit amet</footer>
</div>
</body>
</html>
```